Posters for window front for a Law Firm

Hi everyone,
I need 3 A2 Portrait and 6 A3 Landscape double sided posters designed. The posters are for a shop window front when potential customers come in; they will be able to see the other side hence why I need them double sided.
I have 3 windows, the order will be A2, A3 landscape AND A3 Landscape again
The posters will be fitted on cable displays like estate agents have, I have tried to create a table for you to understand apologies it’s not great. (its attached in a word doc)
We specialise in:
Commercial and residential Conveyancing
Wills and probate
Litigation
Personal injury claims
Landlord and Tenant
Family Law
We need to get our message across to the general public that walk past, that we cover all the above areas of law and more.
Each slot will get an A2 Portrait at the top with an A3 Landscape directly under. There is a frame and then the 2ND a3 landscape poster will sit. There are 3 windows in total each with the above opportunities.
I have attached a file with a photo of the window front
Potential clients that are waking past our shop window front we must stand out but have a commercial professional look. I think the background of each poster will be the same just the wording will differ.
Please do not hesitate in contacting me on 07612384457/07953216608
We have many people walking past which we would like to get the attention directed towards us, at the same time we do not want anything to loud.
Residential

```html
<!DOCTYPE html>
<html lang="en">
<head>
<meta charset="utf-8">
<title>Harcourt Law – Window Poster</title>
<link rel="stylesheet" href="https://fonts.googleapis.com/css2?family=Fira+Sans:wght@400;600&display=swap">
<style>
  :root {
    --navy: #1c2676;
    --gold: #d6c56f;
    --gold-line: #d7b940;
    --gold-text: #d3c068;
    --steel: #6c7fb7;
    --paper: #ffffff;
  }
  html, body {
    margin: 0;
    padding: 0;
    overflow: hidden;
    background: var(--paper);
  }
  .poster {
    position: relative;
    width: 1200px;
    height: 1131px;
    overflow: hidden;
    background: var(--paper);
    font-family: "Fira Sans", "Segoe UI", sans-serif;
  }
  .poster > * { position: absolute; margin: 0; }
  .poster p { margin: 0; }

  .brand-mark {
    left: 66px; top: 66px;
    width: 260px; height: 260px;
    border-radius: 50%;
    background: var(--gold);
  }
  .brand-name {
    left: 430px; top: 82px;
    font-size: 108px;
    font-weight: 400;
    line-height: 1.1;
    letter-spacing: -1px;
    color: var(--navy);
    white-space: nowrap;
  }

  .tiles { display: flex; gap: 10px; }
  .tile { width: 92px; height: 92px; }
  .tile--navy { background: var(--navy); }
  .tile--gold { background: var(--gold); }
  .tiles--top { left: 399px; top: 257px; }
  .tiles--left { left: 0; top: 673px; }
  .tiles--right { left: 805px; top: 649px; gap: 9px; }

  .rule { height: 16px; background: var(--gold-line); }
  .rule--top { left: 257px; top: 358px; width: 541px; }
  .rule--left { left: 0; top: 648px; width: 399px; }
  .rule--right { left: 798px; top: 750px; width: 402px; }

  .photo { display: block; }
  .photo--keys {
    left: 798px; top: 256px; width: 402px; height: 303px;
    background: linear-gradient(120deg, #d9c7bc 0%, #c49b86 35%, #7a5f55 60%, #2c2326 100%);
  }
  .photo--house {
    left: 399px; top: 644px; width: 399px; height: 475px;
    background: linear-gradient(180deg, #8db6e6 0%, #c9dcef 38%, #a48a80 58%, #6f8c4a 82%, #4f7033 100%);
  }

  .service { font-weight: 600; line-height: 1.12; }
  .service--gold { color: var(--gold-text); }
  .service--navy { color: var(--navy); font-weight: 400; }

  .service--injury { left: 40px; top: 408px; font-size: 46px; }
  .service--landlord { left: 459px; top: 398px; font-size: 66px; line-height: 1.1; }
  .service--litigation { left: 47px; top: 568px; font-size: 60px; }
  .service--wills { left: 443px; top: 579px; font-size: 42px; }
  .service--family { left: 871px; top: 581px; font-size: 50px; }
  .service--conveyancing { left: 37px; top: 892px; font-size: 48px; line-height: 1.13; }

  .contact { left: 858px; top: 872px; display: flex; gap: 24px; align-items: flex-start; }
  .contact-icon { width: 78px; height: 58px; margin-top: 10px; flex: none; }
  .contact-number {
    font-size: 64px;
    font-weight: 600;
    line-height: 78px;
    color: var(--steel);
    letter-spacing: 2px;
  }
</style>
</head>
<body>
<main class="poster">
  <div class="brand-mark" aria-hidden="true"></div>
  <h1 class="brand-name">Harcourt Law</h1>

  <div class="tiles tiles--top" aria-hidden="true">
    <span class="tile tile--navy"></span><span class="tile tile--gold"></span><span class="tile tile--navy"></span><span class="tile tile--gold"></span>
  </div>
  <div class="rule rule--top" aria-hidden="true"></div>

  <div class="photo photo--keys" role="img" aria-label="Photo of a smiling man in a suit handing over a set of house keys"></div>

  <p class="service service--gold service--injury">Personal<br>injury claims</p>
  <p class="service service--navy service--landlord">Landlord<br>&amp; Tenant</p>
  <p class="service service--navy service--litigation">Litigation</p>
  <p class="service service--gold service--wills">Wills &amp; probate</p>
  <p class="service service--navy service--family">Family Law</p>

  <div class="rule rule--left" aria-hidden="true"></div>
  <div class="tiles tiles--left" aria-hidden="true">
    <span class="tile tile--navy"></span><span class="tile tile--gold"></span><span class="tile tile--navy"></span><span class="tile tile--gold"></span>
  </div>

  <div class="photo photo--house" role="img" aria-label="Photo of a brick family house under a blue sky with a red estate agent sign post in the front garden"></div>

  <div class="tiles tiles--right" aria-hidden="true">
    <span class="tile tile--navy"></span><span class="tile tile--gold"></span><span class="tile tile--navy"></span><span class="tile tile--gold"></span>
  </div>
  <div class="rule rule--right" aria-hidden="true"></div>

  <p class="service service--gold service--conveyancing">Commercial<br>&amp; residential<br>Conveyancing</p>

  <div class="contact">
    <svg class="contact-icon" viewBox="0 0 78 58" aria-hidden="true">
      <path d="M4 20 C4 6 74 6 74 20 L74 26 L56 26 L56 18 C48 15 30 15 22 18 L22 26 L4 26 Z" fill="var(--steel)"/>
      <path d="M20 28 L58 28 L70 50 C70 54 68 56 64 56 L14 56 C10 56 8 54 8 50 Z" fill="var(--steel)"/>
      <g fill="var(--paper)">
        <rect x="27" y="33" width="6" height="5"/><rect x="36" y="33" width="6" height="5"/><rect x="45" y="33" width="6" height="5"/>
        <rect x="25" y="41" width="6" height="5"/><rect x="36" y="41" width="6" height="5"/><rect x="47" y="41" width="6" height="5"/>
        <rect x="23" y="49" width="6" height="4"/><rect x="36" y="49" width="6" height="4"/><rect x="49" y="49" width="6" height="4"/>
      </g>
    </svg>
    <p class="contact-number">020<br>7946<br>0321</p>
  </div>
</main>
</body>
</html>
```